24Std Betreuung Flyer Senioren
Zielgruppe
Wir vermitteln Ihnen Pflegekräfte aus Polen in 24h Betreuung. Zu diesem Zweck arbeiten wir mit unseren Partnerunternehmen in Polen und Litauen, welche ihre Pflegekraft im Rahmen der EU Dienstleistungsfreiheit legal nach Deutschland vermitteln. Das von uns vermittelte Personal ist freundlich und gut ausgebildet und verfügt über ausreichende bis gute Deutschkenntnisse. Unsere Agentur übernimmt die Koordinierung und Klärung aller Angelegenheiten für die An- und Abreise ihrer Pflegekraft. Das Personal wohnt mit der pflegebürftigen Person zusammen, wodurch wir eine 24h Betreuung realisieren können.
Aufgabenstellung
Seniorengerecht und nicht zu modern, übersichtlich nicht zu klein geschrieben evtl mit lizenzfreien Bildern von Senioren
Format: 6 seitig Wickelfalz
Informationen auf ww.altershilfe-plus.de

```html
<!DOCTYPE html>
<html lang="de">
<head>
<meta charset="utf-8">
<title>24 Std Betreuung – Innenseite</title>
<link href="https://fonts.googleapis.com/css2?family=Arimo:wght@400;700&display=swap" rel="stylesheet">
<style>
  :root {
    --brand-blue: #0a7fc2;
    --text-blue: #14589c;
    --stripe-light: #6fb9e6;
    --stripe-mid: #3396d3;
    --stripe-dark: #0a7fc2;
    --white: #ffffff;
  }
  html, body { margin: 0; padding: 0; overflow: hidden; background: var(--white); }
  .page {
    position: relative; width: 1200px; height: 848px; overflow: hidden;
    background: var(--white);
    font-family: "Arimo", Arial, sans-serif;
  }
  .services-panel {
    position: absolute; left: 0; top: 0; width: 402px; height: 444px;
    background: var(--brand-blue); color: var(--white);
  }
  .services-title {
    position: absolute; left: 46px; top: 46px; margin: 0;
    font-size: 14px; font-weight: 700;
  }
  .check-list { list-style: none; margin: 0; padding: 0; }
  .check-list li {
    position: relative; padding-left: 21px; font-size: 14px; line-height: 17px;
  }
  .check-list svg {
    position: absolute; left: 3px; top: 5px; width: 8px; height: 7px;
  }
  .services-list { position: absolute; left: 46px; top: 76px; width: 350px; }
  .services-list li { margin-bottom: 13px; }
  .services-list li.wrap { line-height: 24px; margin-top: -4px; }
  .services-list li.wrap svg { top: 9px; }

  .hero-photo {
    position: absolute; left: 402px; top: 0; width: 798px; height: 441px;
    background: linear-gradient(100deg, #eef0f1 0%, #e9cfc0 25%, #9fdcd6 45%, #e8c4ae 65%, #f2efea 85%, #e5e3e1 100%);
  }
  .hero-band { position: absolute; left: 402px; top: 444px; width: 798px; height: 14px; background: var(--brand-blue); }
  .side-band { position: absolute; left: 0; top: 462px; width: 402px; height: 7px; background: var(--brand-blue); }

  .walker-photo {
    position: absolute; left: 0; top: 478px; width: 402px; height: 315px;
    background: linear-gradient(120deg, #a9c79a 0%, #e8d6cc 35%, #7fd0c6 60%, #c7b3a6 80%, #cfcfcf 100%);
  }

  .info-column { position: absolute; color: var(--text-blue); }
  .info-column h2 { margin: 0; font-size: 14px; font-weight: 700; line-height: 20px; }
  .info-column .check-list { position: absolute; left: 0; width: 360px; }
  .info-column .check-list li { line-height: 30px; }
  .info-column .check-list svg { top: 12px; }
  .info-column .check-list .sub { display: block; padding-left: 2px; }
  .cost-factors { left: 437px; top: 493px; }
  .care-promise { left: 835px; top: 512px; }
  .cost-factors .check-list { top: 78px; }
  .care-promise .check-list { top: 58px; }

  .stripe { position: absolute; left: 0; width: 1200px; }
  .stripe-light { top: 799px; height: 8px; background: var(--stripe-light); }
  .stripe-mid { top: 813px; height: 14px; background: var(--stripe-mid); }
  .stripe-dark { top: 832px; height: 16px; background: var(--stripe-dark); }
</style>
</head>
<body>
<svg width="0" height="0" style="position:absolute">
  <defs>
    <symbol id="tick" viewBox="0 0 8 7"><path d="M0.8 3.6 L3 5.8 L7.2 1" fill="none" stroke="currentColor" stroke-width="1.8"/></symbol>
  </defs>
</svg>
<main class="page">
  <section class="services-panel">
    <h2 class="services-title">Unsere Dienstleistungen</h2>
    <ul class="check-list services-list">
      <li><svg><use href="#tick"/></svg>legales Pflegepersonal&nbsp; (A1-Bescheinigung)</li>
      <li><svg><use href="#tick"/></svg>bezahlbare Alternative zum Pflegeheim</li>
      <li><svg><use href="#tick"/></svg>mehrere Kooperationspartner aus Osteuropa</li>
      <li><svg><use href="#tick"/></svg>deutschsprachige Betreuer/ innen</li>
      <li><svg><use href="#tick"/></svg>langjährige Erfahrung</li>
      <li><svg><use href="#tick"/></svg>kostenfreier Besichtigungstermin</li>
      <li><svg><use href="#tick"/></svg>zielgerichtete Beratung vor Ort</li>
      <li><svg><use href="#tick"/></svg>individuelles und unverbindliches Angebot</li>
      <li class="wrap"><svg><use href="#tick"/></svg>Koordination und Organisation der gesamten Auftragsabwicklung</li>
      <li><svg><use href="#tick"/></svg>höchste Flexibilität<br>(Vermittlung innerhalb weniger Tage)</li>
    </ul>
  </section>

  <div class="hero-photo" role="img" aria-label="Foto: lächelnde Pflegerin mit Stethoskop neben einer lächelnden Seniorin"></div>
  <div class="hero-band"></div>
  <div class="side-band"></div>
  <div class="walker-photo" role="img" aria-label="Foto: Pflegerin stützt eine Seniorin am Rollator"></div>

  <section class="info-column cost-factors">
    <h2>Die Gesamtkosten der 24 Std Pflege<br>sind von folgenden Faktoren abhängig:</h2>
    <ul class="check-list">
      <li><svg><use href="#tick"/></svg>Schwierigkeit der Betreuung ist nicht<span class="sub">zwingend abhängig vom Pflegegrad</span></li>
      <li><svg><use href="#tick"/></svg>Anforderung an die Betreuerin<span class="sub">( Sprachkenntnisse, Pflege-Erfahrungen...)</span></li>
      <li><svg><use href="#tick"/></svg>Anzahl der im Haushalt zu pflegenden Personen</li>
      <li><svg><use href="#tick"/></svg>Anzahl von nächtlichen Einsätzen</li>
    </ul>
  </section>

  <section class="info-column care-promise">
    <h2>Wir kümmern uns um Sie</h2>
    <ul class="check-list">
      <li><svg><use href="#tick"/></svg>Schwierigkeit der Betreuung ist nicht<span class="sub">zwingend abhängig vom Pflegegrad</span></li>
      <li><svg><use href="#tick"/></svg>Anforderung an die Betreuerin<span class="sub">( Sprachkenntnisse, Pflege-Erfahrungen...)</span></li>
      <li><svg><use href="#tick"/></svg>Anzahl der im Haushalt zu pflegenden Personen</li>
      <li><svg><use href="#tick"/></svg>Anzahl von nächtlichen Einsätzen</li>
    </ul>
  </section>

  <div class="stripe stripe-light"></div>
  <div class="stripe stripe-mid"></div>
  <div class="stripe stripe-dark"></div>
</main>
</body>
</html>
```